Graphic to show easy steps to find financial clarity

Howdy-I need a graphic that describe my Coin Harbor Method.The attached is a concept, but please use your own creativity to show how you would display this:- There are 5 steps the process (and then we repeat/recalculate)- And three bullets that drive home the results of the processI've also attached my logo. Please use the colors in my logo and maybe add a soft green as needed.The reader should be able to briefly scan this document and understand that this is an easy/simple process that tells them how to manage their cash.Thanks!-Ned

Target Market(s)

wealthy women, whether single or married

Requirements
Must have
• Please use the colors in my logo and a soft green if needed
Should not have
• This should be a very easy to read graphic that communicates how simple/easy this is to do.

```html
<!DOCTYPE html>
<html lang="en">
<head>
<meta charset="utf-8">
<title>Coin Harbor Method</title>
<link href="https://fonts.googleapis.com/css2?family=Montserrat:wght@600;700;800&family=Open+Sans:wght@600&display=swap" rel="stylesheet">
<style>
  :root {
    --navy: #1f3a78;
    --navy-deep: #17305f;
    --step2: #17629c;
    --step3: #0f78b5;
    --step4: #0d90c4;
    --step5: #10b2e3;
    --step6: #72cbe9;
    --step6-cap: #58afc6;
    --teal: #16b1b8;
    --text-dark: #2b2b33;
    --arrow: #3a3d44;
    --line: #9aa0a6;
    --bg: #ffffff;
  }
  * { margin: 0; padding: 0; box-sizing: border-box; }
  html, body { width: 1200px; height: 865px; overflow: hidden; background: var(--bg); }
  .canvas { position: relative; width: 1200px; height: 865px; background: var(--bg); }

  .texture {
    position: absolute; right: 0; top: 0; width: 560px; height: 430px;
    background: radial-gradient(ellipse at 78% 30%, rgba(150,165,180,0.18) 0%, rgba(150,165,180,0.06) 45%, rgba(255,255,255,0) 70%);
  }

  .brand {
    position: absolute; left: 74px; top: 96px;
    display: flex; align-items: center; gap: 14px;
  }
  .brand-mark { width: 40px; height: 40px; background: var(--navy); }
  .brand-name {
    font-family: "Montserrat", sans-serif; font-weight: 700;
    font-size: 21px; color: var(--navy); line-height: 1.15; letter-spacing: 0.3px;
  }

  .title-rule { position: absolute; left: 946px; top: 101px; width: 122px; height: 5px; background: var(--teal); }
  .title {
    position: absolute; right: 132px; top: 118px;
    font-family: "Montserrat", sans-serif; font-size: 28px; color: var(--navy);
    letter-spacing: 0.5px; font-weight: 600;
  }
  .title strong { font-weight: 800; }

  .steps { position: absolute; left: 0; top: 0; }
  .step-label {
    font-family: "Montserrat", sans-serif; font-weight: 800; fill: #ffffff;
    font-size: 13.5px; text-anchor: middle; letter-spacing: 0.2px;
  }
  .step-number {
    font-family: "Montserrat", sans-serif; font-weight: 600; fill: #ffffff;
    font-size: 17px; text-anchor: middle;
  }

  .result {
    position: absolute; width: 250px; text-align: center;
    font-family: "Open Sans", sans-serif; font-weight: 600;
    font-size: 16.5px; line-height: 1.32; color: var(--text-dark);
  }
  .result-lifestyle { left: 169px; top: 512px; }
  .result-base { left: 463px; top: 526px; }
  .result-joy { left: 740px; top: 540px; }
</style>
</head>
<body>
<main class="canvas">
  <div class="texture" role="img" aria-label="Soft dotted background texture"></div>

  <div class="brand">
    <div class="brand-mark"></div>
    <div class="brand-name">Kestrel Lane<br>Advisory, LLC</div>
  </div>

  <div class="title-rule"></div>
  <h1 class="title"><strong>COIN HARBOR</strong> METHOD</h1>

  <svg class="steps" width="1200" height="865" viewBox="0 0 1200 865">
    <defs>
      <clipPath id="c1"><circle cx="168" cy="352" r="80"/></clipPath>
      <clipPath id="c2"><circle cx="337" cy="352" r="80"/></clipPath>
      <clipPath id="c3"><circle cx="506" cy="352" r="80"/></clipPath>
      <clipPath id="c4"><circle cx="675" cy="352" r="80"/></clipPath>
      <clipPath id="c5"><circle cx="843" cy="352" r="80"/></clipPath>
      <clipPath id="c6"><circle cx="1017" cy="352" r="78"/></clipPath>
    </defs>

    <g class="step">
      <circle cx="168" cy="352" r="80" fill="var(--navy)"/>
      <rect x="80" y="270" width="180" height="42" fill="var(--navy-deep)" clip-path="url(#c1)"/>
      <text class="step-number" x="168" y="300">01</text>
      <text class="step-label" x="168" y="362">KNOW YOUR</text>
      <text class="step-label" x="168" y="379">ANNUAL</text>
      <text class="step-label" x="168" y="396">SPENDING</text>
    </g>
    <g class="step">
      <circle cx="337" cy="352" r="80" fill="var(--step2)"/>
      <rect x="250" y="270" width="180" height="42" fill="#12507f" clip-path="url(#c2)"/>
      <text class="step-number" x="337" y="300">02</text>
      <text class="step-label" x="337" y="352">PROJECT</text>
      <text class="step-label" x="337" y="369">SPECIAL</text>
      <text class="step-label" x="337" y="386">EXPENSES</text>
    </g>
    <g class="step">
      <circle cx="506" cy="352" r="80" fill="var(--step3)"/>
      <rect x="420" y="270" width="180" height="42" fill="#0c6497" clip-path="url(#c3)"/>
      <text class="step-number" x="506" y="300">03</text>
      <text class="step-label" x="506" y="352">ADD UP</text>
      <text class="step-label" x="506" y="369">YOUR 5-YEAR</text>
      <text class="step-label" x="506" y="386">CASH NEEDS</text>
    </g>
    <g class="step">
      <circle cx="675" cy="352" r="80" fill="var(--step4)"/>
      <rect x="590" y="270" width="180" height="42" fill="#0b7aa6" clip-path="url(#c4)"/>
      <text class="step-number" x="675" y="300">04</text>
      <text class="step-label" x="675" y="352">SET THEM</text>
      <text class="step-label" x="675" y="369">ASIDE IN</text>
      <text class="step-label" x="675" y="386">SAVINGS</text>
    </g>
    <g class="step">
      <circle cx="843" cy="352" r="80" fill="var(--step5)"/>
      <rect x="760" y="270" width="180" height="42" fill="#0d99c4" clip-path="url(#c5)"/>
      <text class="step-number" x="843" y="300">05</text>
      <text class="step-label" x="843" y="362">INVEST</text>
      <text class="step-label" x="843" y="379">THE REST</text>
    </g>
    <g class="step">
      <circle cx="1017" cy="352" r="78" fill="var(--step6)"/>
      <rect x="930" y="272" width="180" height="40" fill="var(--step6-cap)" clip-path="url(#c6)"/>
      <text class="step-number" x="1017" y="300" style="font-size:15px;font-weight:700">REPEAT</text>
      <text class="step-label" x="1017" y="362">RECALCULATE</text>
      <text class="step-label" x="1017" y="379">MONTHLY</text>
    </g>

    <g class="connectors" fill="var(--arrow)">
      <circle cx="251" cy="368" r="14" stroke="#fff" stroke-width="2"/>
      <circle cx="420" cy="368" r="14" stroke="#fff" stroke-width="2"/>
      <circle cx="589" cy="368" r="14" stroke="#fff" stroke-width="2"/>
      <circle cx="758" cy="368" r="14" stroke="#fff" stroke-width="2"/>
      <circle cx="929" cy="368" r="14" stroke="#fff" stroke-width="2"/>
    </g>
    <g class="connector-arrows" fill="#ffffff">
      <path d="M247 361 L257 368 L247 375 Z"/>
      <path d="M416 361 L426 368 L416 375 Z"/>
      <path d="M585 361 L595 368 L585 375 Z"/>
      <path d="M754 361 L764 368 L754 375 Z"/>
      <path d="M925 361 L935 368 L925 375 Z"/>
    </g>

    <line class="timeline" x1="84" y1="717" x2="1092" y2="717" stroke="var(--line)" stroke-width="1.5" stroke-dasharray="1.5 3"/>

    <g class="result-icon">
      <path d="M263 632 h60 v38 h-22 l-8 9 l-8 -9 h-22 Z" fill="var(--teal)"/>
      <path d="M293 662 c-12 -8 -16 -13 -16 -18 c0 -5 4 -8 8 -8 c4 0 7 3 8 5 c1 -2 4 -5 8 -5 c4 0 8 3 8 8 c0 5 -4 10 -16 18 Z" fill="#fff"/>
      <circle cx="293" cy="717" r="7" fill="#fff" stroke="var(--arrow)" stroke-width="1.5"/>
      <circle cx="293" cy="717" r="3.5" fill="var(--arrow)"/>
    </g>
    <g class="result-icon">
      <path d="M558 632 h60 v38 h-22 l-8 9 l-8 -9 h-22 Z" fill="var(--teal)"/>
      <text x="588" y="661" text-anchor="middle" font-family="Montserrat, sans-serif" font-weight="700" font-size="24" fill="#fff">$</text>
      <circle cx="588" cy="717" r="7" fill="#fff" stroke="var(--arrow)" stroke-width="1.5"/>
      <circle cx="588" cy="717" r="3.5" fill="var(--arrow)"/>
    </g>
    <g class="result-icon">
      <path d="M833 632 h60 v38 h-22 l-8 9 l-8 -9 h-22 Z" fill="var(--teal)"/>
      <path d="M853 640 h14 v4 h-10 v16 h10 v4 h-14 Z" fill="#fff"/>
      <path d="M863 650 h10 v-5 l9 7 l-9 7 v-5 h-10 Z" fill="#fff"/>
      <circle cx="863" cy="717" r="7" fill="#fff" stroke="var(--arrow)" stroke-width="1.5"/>
      <circle cx="863" cy="717" r="3.5" fill="var(--arrow)"/>
    </g>
  </svg>

  <p class="result result-lifestyle">Know your lifestyle will be unaffected by the markets for at least 5-years</p>
  <p class="result result-base">Create a solid base for lifetime cash flow projections</p>
  <p class="result result-joy">Spend intentionally<br>and with job</p>
</main>
</body>
</html>
```